Harlune Painting

Need business card design

Target Market(s)

Paint

Industry/Entity Type

Painting

Requirements
Must have
• Brice Halvorn | Superviser
| HarLune Painting
| mobile: (360) 555-0148
| email: Brice@harluneinc.example
| site: www.harluneinc.example
| address: 718 Corliss Rd NE Ste 300, Olympia, WA 98501

```html
<!DOCTYPE html>
<html lang="en">
<head>
<meta charset="utf-8">
<title>HarLune Painting – Business Card</title>
<link href="https://fonts.googleapis.com/css2?family=Libre+Baskerville:wght@700&family=Roboto:wght@400&display=swap" rel="stylesheet">
<style>
  :root {
    --navy: #22407f;
    --green: #62b946;
    --white: #ffffff;
    --ink: #2b2b2b;
    --backdrop: #d6d6d6;
  }
  * { margin: 0; padding: 0; box-sizing: border-box; }
  html, body { width: 1200px; height: 852px; overflow: hidden; background: var(--backdrop); }
  .stage { position: relative; width: 1200px; height: 852px; }

  .card {
    position: absolute;
    width: 540px; height: 309px;
    border-radius: 22px;
    overflow: hidden;
    box-shadow: 0 4px 10px rgba(0,0,0,.18);
  }

  /* Front */
  .card--front { left: 40px; top: 90px; background: var(--navy); }
  .brand {
    font-family: "Libre Baskerville", Georgia, serif;
    font-weight: 700;
    display: flex; align-items: center; gap: 12px;
  }
  .card--front .brand {
    position: absolute; inset: 0;
    justify-content: center;
    color: var(--white);
    font-size: 30px;
  }
  .brand__dot { width: 16px; height: 16px; border-radius: 50%; background: var(--green); flex: none; }

  /* Back */
  .card--back { left: 620px; top: 450px; background: var(--white); }
  .card--back .swoosh { position: absolute; inset: 0; width: 100%; height: 100%; }
  .card--back .brand {
    position: absolute; left: 34px; top: 100px; width: 220px;
    color: var(--navy); font-size: 21px; line-height: 1.2;
  }
  .divider { position: absolute; left: 268px; top: 54px; width: 1.5px; height: 124px; background: var(--green); }

  .contact {
    position: absolute; left: 284px; top: 44px;
    font-family: "Roboto", Arial, sans-serif; color: var(--ink);
    font-size: 12.5px; line-height: 1.45;
  }
  .contact__name {
    font-family: "Libre Baskerville", Georgia, serif; font-weight: 700;
    font-size: 17px; color: var(--navy); letter-spacing: .5px; line-height: 1.2;
  }
  .contact__name .surname { color: var(--green); }
  .contact__title { margin-bottom: 2px; }
  .contact__row { display: flex; align-items: center; gap: 6px; }
  .contact__row svg { width: 10px; height: 10px; fill: var(--navy); flex: none; }
  .accent { color: var(--green); }
</style>
</head>
<body>
<main class="stage">

  <section class="card card--front" aria-label="Card front">
    <div class="brand"><span class="brand__dot"></span>HarLune Painting</div>
  </section>

  <section class="card card--back" aria-label="Card back">
    <svg class="swoosh" viewBox="0 0 540 309" preserveAspectRatio="none" aria-hidden="true">
      <path d="M0 265 C220 260 440 235 540 160 L540 309 L0 309 Z" fill="var(--navy)"/>
      <path d="M190 258 C360 252 460 228 540 153" fill="none" stroke="var(--white)" stroke-width="6"/>
      <path d="M200 255 C360 248 460 222 540 147" fill="none" stroke="var(--green)" stroke-width="4"/>
      <path d="M230 251 C380 243 465 214 540 138" fill="none" stroke="var(--navy)" stroke-width="3"/>
    </svg>

    <div class="brand"><span class="brand__dot"></span>HarLune Painting</div>
    <div class="divider"></div>

    <div class="contact">
      <div class="contact__name">BRICE <span class="surname">HALVORN</span></div>
      <div class="contact__title">Superviser</div>
      <div>718 Corliss Rd NE Ste 300,</div>
      <div>Olympia, WA 98501</div>
      <div class="contact__row">
        <svg viewBox="0 0 10 10"><path d="M2 0.5 L3.6 2.6 L2.7 3.6 C3.3 5 4.9 6.6 6.4 7.3 L7.4 6.4 L9.5 8 L8.3 9.5 C4.5 9.2 0.8 5.5 0.5 1.7 Z"/></svg>
        (360) 555-0148
      </div>
      <div class="contact__row">
        <svg viewBox="0 0 10 10"><path d="M0 2 H10 V8.5 H0 Z M0.6 2.5 L5 5.8 L9.4 2.5" fill="var(--navy)" stroke="var(--white)" stroke-width="0.8"/></svg>
        Brice@harluneinc.example
      </div>
      <div class="contact__row">
        <svg viewBox="0 0 10 10"><circle cx="5" cy="5" r="4.5"/><path d="M0.5 5 H9.5 M5 0.5 C2.8 3 2.8 7 5 9.5 M5 0.5 C7.2 3 7.2 7 5 9.5" fill="none" stroke="var(--white)" stroke-width="0.7"/></svg>
        <span>www.<span class="accent">harluneinc</span>.example</span>
      </div>
    </div>
  </section>

</main>
</body>
</html>
```